Awesome business card design needed

We need a new business card design to go with our new logo.
We are a web development agency that specialises in highly complex back-end integrations as opposed to design, our customers are retailers, hotels, hospitals and any other organisation that has a large online marketing department.
Take a look at our website - www.orvekplus.com for some inspiration.
We want our new business cards to exude class, professionalism and style.
We are likely to choose a high-end card to print them on but we want the design of the card itself to really turn heads.
We have no specific colour requirements, the logo as you will see is a turquoise colour R89 G171 B167 #59aba7 but it can also be in white if you want to make the colour of the card something different.
The information on the card should be:
Name
Position
Tel
email
Potentially a double sided card could have our web address, twitter and FB links.

```html
<!DOCTYPE html>
<html lang="en">
<head>
<meta charset="utf-8">
<title>Orvek Plus – Team Card</title>
<link rel="stylesheet" href="https://fonts.googleapis.com/css2?family=Codystar:wght@400&family=Source+Sans+3:wght@400&display=swap">
<style>
  :root {
    --card-teal: #4aaba6;
    --tile-teal: #58b6b1;
    --tone-dark: #3d4a52;
    --tone-warm: #7a6650;
    --tone-light: #c9d3d6;
    --tone-red: #8e4a45;
    --tone-blue: #5f7f9e;
    --ink-white: #ffffff;
  }
  html, body {
    margin: 0;
    padding: 0;
    width: 1200px;
    height: 634px;
    overflow: hidden;
    background: var(--card-teal);
  }
  .card {
    position: relative;
    width: 1200px;
    height: 634px;
    background: var(--card-teal);
    color: var(--ink-white);
    overflow: hidden;
  }
  .team-grid {
    position: absolute;
    left: 42px;
    top: 70px;
    display: grid;
    grid-template-columns: 142px 142px;
    grid-template-rows: 144px 144px 144px;
    column-gap: 56px;
    row-gap: 32px;
  }
  .team-portrait {
    width: 142px;
    height: 144px;
  }
  .portrait-1 { background: linear-gradient(180deg, var(--tile-teal) 0%, var(--tone-dark) 100%); }
  .portrait-2 { background: linear-gradient(180deg, var(--tone-warm) 0%, var(--tone-blue) 100%); }
  .portrait-3 { background: linear-gradient(180deg, var(--tone-light) 0%, var(--tone-red) 100%); }
  .portrait-4 { background: linear-gradient(180deg, var(--tone-red) 0%, var(--tone-dark) 100%); }
  .portrait-5 { background: linear-gradient(180deg, var(--tone-warm) 0%, var(--tone-dark) 100%); }
  .portrait-6 { background: linear-gradient(180deg, var(--tone-dark) 0%, var(--tone-blue) 100%); }

  .headline {
    position: absolute;
    left: 402px;
    top: 58px;
    margin: 0;
    font-family: "Codystar", "Source Sans 3", sans-serif;
    font-weight: 400;
    line-height: 1;
  }
  .headline-lead {
    display: block;
    font-size: 112px;
    letter-spacing: 2px;
  }
  .headline-rest {
    display: block;
    font-size: 54px;
    line-height: 80px;
    margin-top: -4px;
    letter-spacing: 1px;
  }
  .divider {
    position: absolute;
    left: 402px;
    top: 411px;
    width: 746px;
    height: 2px;
    background: var(--ink-white);
  }
  .contact-list {
    position: absolute;
    left: 402px;
    top: 432px;
    margin: 0;
    padding: 0;
    list-style: none;
    font-family: "Source Sans 3", sans-serif;
    font-size: 33px;
    line-height: 48px;
  }
</style>
</head>
<body>
  <main class="card">
    <section class="team-grid">
      <div class="team-portrait portrait-1" role="img" aria-label="Cartoon portrait of a team member in a black tuxedo and bow tie"></div>
      <div class="team-portrait portrait-2" role="img" aria-label="Cartoon portrait of a team member with brown hair in a blue checked shirt"></div>
      <div class="team-portrait portrait-3" role="img" aria-label="Cartoon portrait of a white-haired bearded team member in a red checked shirt"></div>
      <div class="team-portrait portrait-4" role="img" aria-label="Cartoon portrait of a team member in a red cap and varsity jacket"></div>
      <div class="team-portrait portrait-5" role="img" aria-label="Cartoon portrait of a grinning team member with headphones round his neck"></div>
      <div class="team-portrait portrait-6" role="img" aria-label="Cartoon portrait of a bearded team member in a striped blue shirt"></div>
    </section>

    <h1 class="headline">
      <span class="headline-lead">Ours</span>
      <span class="headline-rest">is a team of truly</span>
      <span class="headline-rest">special people...</span>
    </h1>

    <div class="divider"></div>

    <ul class="contact-list">
      <li>info@orvekplus.com</li>
      <li>https://www.friendwall.net/OrvekPlus?filter=1</li>
      <li>https://chirpline.net/orvekplus</li>
    </ul>
  </main>
</body>
</html>
```